Brandt Family Motto/Mission Statement

We are creating a poster to be hung in our home with several purpose statements for our family (last name Brandt, and "The Brandt Family" should be included in the poster prominently). The text that we want included is in the attached file.

Our kids range in age from 8 to 17, so we are looking for something that is homey and cheerful, but fairly bold and oriented to older kids (and not so much younger kids).

I've attached a couple of example poster/statements that we generally like. Overall color scheme could include blues and greens and possibly some brown.

Anticipated size of this poster would be 18"x24" with a portrait orientation.

```html
<!DOCTYPE html>
<html lang="en">
<head>
<meta charset="utf-8">
<title>The Brandt Family – Purpose Statements</title>
<link rel="stylesheet" href="https://fonts.googleapis.com/css2?family=Roboto+Condensed:wght@300;400;700&display=swap">
<style>
  :root {
    --backdrop: #d9dadf;
    --paper: #ffffff;
    --green: #009140;
    --sky-1: #4db8ec;
    --sky-2: #6cc3ef;
    --blue-1: #0aa2e0;
    --blue-2: #0c8fd7;
    --blue-3: #0a78c0;
    --blue-4: #0d5ea8;
    --navy: #173f8e;
    --gold: #f7b500;
    --ink-light: #ffffff;
    --icon-tone: rgba(255, 255, 255, 0.22);
  }
  * { margin: 0; padding: 0; box-sizing: border-box; }
  html, body { width: 1200px; height: 1000px; overflow: hidden; }
  body {
    background: var(--backdrop);
    font-family: "Roboto Condensed", "Arial Narrow", sans-serif;
    position: relative;
  }
  .poster {
    position: absolute;
    left: 270px; top: 52px;
    width: 673px; height: 898px;
    background: var(--paper);
    overflow: hidden;
  }
  .panel {
    position: absolute;
    overflow: hidden;
    color: var(--ink-light);
  }
  .statement {
    position: absolute;
    font-weight: 300;
    font-size: 30px;
    line-height: 32px;
    color: var(--ink-light);
    z-index: 3;
  }
  .statement strong { font-weight: 700; color: var(--gold); }
  .icon {
    position: absolute;
    border-radius: 6px;
    background: var(--icon-tone);
    z-index: 3;
  }
  .title-panel { left: 19px; top: 19px; width: 376px; height: 166px; background: var(--green); }
  .family-name {
    position: absolute;
    left: 0; right: 0; top: 50%;
    transform: translateY(-50%);
    text-align: center;
    font-weight: 700;
    font-size: 52px;
    line-height: 1;
    letter-spacing: 1px;
    text-transform: uppercase;
    color: var(--gold);
  }
  .watermark {
    position: absolute;
    left: 210px; top: 250px;
    transform-origin: left top;
    transform: rotate(90deg) translateY(-100%);
    font-weight: 700;
    font-size: 120px;
    line-height: 104px;
    text-transform: uppercase;
    color: rgba(255, 255, 255, 0.16);
    white-space: nowrap;
    z-index: 2;
    pointer-events: none;
  }
  .learn { left: 19px; top: 189px; width: 376px; height: 169px; background: var(--sky-1); }
  .adventure { left: 400px; top: 19px; width: 255px; height: 339px; background: var(--sky-2); }
  .kindness { left: 19px; top: 362px; width: 376px; height: 175px; background: var(--blue-1); }
  .fit { left: 400px; top: 362px; width: 255px; height: 175px; background: var(--blue-2); }
  .right-thing { left: 19px; top: 541px; width: 253px; height: 339px; background: var(--blue-3); }
  .humor { left: 277px; top: 541px; width: 378px; height: 167px; background: var(--blue-4); }
  .positive { left: 277px; top: 712px; width: 378px; height: 168px; background: var(--navy); }
  .centered { text-align: center; }
  .right-aligned { text-align: right; }
</style>
</head>
<body>
  <main class="poster">
    <section class="panel title-panel">
      <h1 class="family-name">The Brandt Family</h1>
    </section>

    <section class="panel learn">
      <p class="statement" style="left:34px; top:36px;">We <strong>love</strong><br>to learn<br>new things.</p>
      <div class="icon" role="img" aria-label="Open book icon" style="left:226px; top:50px; width:86px; height:70px;"></div>
    </section>

    <section class="panel adventure">
      <div class="icon" role="img" aria-label="Hiker climbing a mountain slope icon" style="left:56px; top:22px; width:138px; height:130px;"></div>
      <p class="statement centered" style="left:0; right:0; top:160px;">We create<br><strong>adventure</strong><br>and choose<br>experiences<br>over things</p>
    </section>

    <section class="panel kindness">
      <div class="icon" role="img" aria-label="Lit candle icon" style="left:34px; top:38px; width:36px; height:96px;"></div>
      <p class="statement" style="left:101px; top:40px;"><strong>Kindness</strong><br>guides our words<br>and deeds.</p>
    </section>

    <section class="panel fit">
      <p class="statement" style="left:26px; top:40px;">We<br>commit<br>to be <strong>fit</strong>.</p>
      <div class="icon" role="img" aria-label="Person lifting dumbbells icon" style="left:150px; top:40px; width:88px; height:86px;"></div>
    </section>

    <section class="panel right-thing">
      <div class="icon" role="img" aria-label="Thumbs up icon" style="left:96px; top:30px; width:62px; height:70px;"></div>
      <p class="statement centered" style="left:0; right:0; top:118px;">We <strong>do<br>what is<br>right</strong><br>even when<br>no one is<br>watching.</p>
    </section>

    <section class="panel humor">
      <div class="icon" role="img" aria-label="Smiley icon" style="left:26px; top:52px; width:66px; height:66px; border-radius:50%;"></div>
      <p class="statement right-aligned" style="right:28px; top:36px;">Our days are<br>brightened by a<br><strong>sense of humor</strong>.</p>
    </section>

    <section class="panel positive">
      <p class="statement" style="left:26px; top:30px;">We look at<br>life through<br>a <strong>positive</strong> lens.</p>
      <div class="icon" role="img" aria-label="Eye icon" style="left:262px; top:56px; width:90px; height:54px; border-radius:50%;"></div>
    </section>

    <div class="watermark" aria-hidden="true">The<br>Brandt<br>Family</div>
  </main>
</body>
</html>
```